Quillon Maison Wood Fired Pizza business card design

I have a logo and need an eye catching design that will get me noticed.
My business is wood fired pizza. I want a bold design that will make our customers remember us and the food that we serve. Work with the colors of our logo and texts. Maybe add designs that lend to what or how pizza is made using our wood fired oven?

Target Market(s)

Foodies!

Contact Information for Business Card

Quillon Maison Wood Fired Pizza
Our slogan is Fast. Fresh. Handcrafted
Catering for all events

Requirements
Must have
• Dana Porrick
Telephone 570 555 0183
website www.getquillon.example
Facebook @getquillonpizza maybe use the facebook logo next to it
Instagram getquillonpizza maybe use the instagram logo next to it
Catering for all events
Nice to have
• Maybe pizza peels, pizza cutters? Wood? Fired wood? Using our flame in the background?
Please work with different colored text so each sentence stands out? A themed color for facebook?
Maybe work with the colors within our logo?
Please try to use the our quillon font, but not a must have.

```html
<!DOCTYPE html>
<html lang="en">
<head>
<meta charset="utf-8">
<title>Quillon Maison Wood Fired Pizza – Business Card</title>
<link rel="stylesheet" href="https://fonts.googleapis.com/css2?family=Lato:wght@400;700;900&display=swap">
<style>
  :root {
    --stage: #d2d2cd;
    --card: #14161f;
    --ember: #d42027;
    --ash: #ffffff;
    --ash-soft: #b9bac0;
    --photo-dark: #1c1a20;
    --photo-warm: #3a2a2c;
  }
  * { box-sizing: border-box; margin: 0; padding: 0; }
  html, body { width: 1200px; height: 801px; overflow: hidden; }
  body {
    background: var(--stage);
    font-family: "Lato", sans-serif;
    display: flex;
    align-items: center;
    justify-content: center;
    gap: 40px;
  }
  .card {
    width: 540px;
    height: 309px;
    background: var(--card);
    position: relative;
    overflow: hidden;
    box-shadow: 0 10px 24px rgba(0,0,0,0.25);
  }

  /* Front: contact side */
  .card-front { display: flex; align-items: center; }
  .brand-block {
    width: 50%;
    display: flex;
    align-items: center;
    justify-content: center;
    gap: 10px;
  }
  .brand-dot {
    width: 14px; height: 14px;
    border-radius: 50%;
    background: var(--ember);
    flex: none;
  }
  .brand-name {
    color: var(--ash);
    font-weight: 900;
    font-size: 22px;
    letter-spacing: 2px;
    line-height: 1.1;
  }
  .divider {
    width: 2px;
    height: 150px;
    background: var(--ember);
    flex: none;
  }
  .contact-block { padding-left: 26px; }
  .person-name {
    color: var(--ember);
    font-weight: 900;
    font-size: 26px;
    letter-spacing: 1px;
    line-height: 1.1;
    text-transform: uppercase;
  }
  .person-role {
    color: var(--ash);
    font-size: 15px;
    margin: 3px 0 12px;
  }
  .contact-list { list-style: none; }
  .contact-item {
    display: flex;
    align-items: center;
    gap: 10px;
    color: var(--ash);
    font-size: 14px;
    line-height: 22px;
    white-space: nowrap;
  }
  .contact-icon { width: 14px; height: 14px; flex: none; }
  .service-note {
    margin-top: 12px;
    color: var(--ember);
    font-size: 12px;
    font-weight: 700;
    letter-spacing: 0.5px;
  }
  .slogan {
    margin-top: 2px;
    color: var(--ash-soft);
    font-size: 12px;
    letter-spacing: 0.5px;
  }

  /* Back: brand side */
  .card-back { display: flex; align-items: center; justify-content: center; }
  .photo-fill {
    position: absolute; inset: 0;
    background: radial-gradient(ellipse at 55% 60%, var(--photo-warm) 0%, var(--photo-dark) 70%);
  }
  .back-brand {
    position: relative;
    display: flex;
    align-items: center;
    gap: 14px;
  }
  .back-brand .brand-dot { width: 22px; height: 22px; }
  .back-brand .brand-name { font-size: 40px; letter-spacing: 4px; }
</style>
</head>
<body>
  <section class="card card-front">
    <div class="brand-block">
      <span class="brand-dot"></span>
      <span class="brand-name">QUILLON<br>MAISON</span>
    </div>
    <div class="divider"></div>
    <div class="contact-block">
      <h1 class="person-name">Dana Porrick</h1>
      <p class="person-role">Owner</p>
      <ul class="contact-list">
        <li class="contact-item">
          <svg class="contact-icon" viewBox="0 0 24 24"><path fill="var(--ember)" d="M6.6 10.8a15 15 0 0 0 6.6 6.6l2.2-2.2a1 1 0 0 1 1-.25 11.4 11.4 0 0 0 3.6.57 1 1 0 0 1 1 1V20a1 1 0 0 1-1 1A17 17 0 0 1 3 4a1 1 0 0 1 1-1h3.5a1 1 0 0 1 1 1c0 1.25.2 2.45.57 3.57a1 1 0 0 1-.25 1z"/></svg>
          570 555 0183
        </li>
        <li class="contact-item">
          <svg class="contact-icon" viewBox="0 0 24 24" fill="none" stroke="var(--ember)" stroke-width="2"><circle cx="12" cy="12" r="10"/><path d="M2 12h20M12 2a15 15 0 0 1 0 20M12 2a15 15 0 0 0 0 20"/></svg>
          www.getquillon.example
        </li>
        <li class="contact-item">
          <svg class="contact-icon" viewBox="0 0 24 24" fill="none" stroke="var(--ember)" stroke-width="2"><circle cx="12" cy="12" r="10"/><path d="M7 8.5h10v6h-5l-3 2.5v-2.5H7z" stroke-linejoin="round"/></svg>
          @getquillonpizza
        </li>
        <li class="contact-item">
          <svg class="contact-icon" viewBox="0 0 24 24" fill="none" stroke="var(--ember)" stroke-width="2"><circle cx="12" cy="12" r="10"/><path d="M10 7l-1.5 10M15.5 7L14 17M7.5 10h10M6.5 14h10"/></svg>
          @getquillonpizza
        </li>
      </ul>
      <p class="service-note">Catering for all events</p>
      <p class="slogan">Fast. Fresh. Handcrafted.</p>
    </div>
  </section>

  <section class="card card-back">
    <div class="photo-fill" role="img" aria-label="Dimmed photo of a wood fired pizza on a wooden table being sliced"></div>
    <div class="back-brand">
      <span class="brand-dot"></span>
      <span class="brand-name">QUILLON<br>MAISON</span>
    </div>
  </section>
</body>
</html>
```